Nordisk Husforum

Company is in: Denmark - Copenhagen
It sells: Restaurants and café buildings
Companys age: 25 years
Main benefit: trust with over 25 years experience

```html
<!DOCTYPE html>
<html lang="en">
<head>
<meta charset="utf-8">
<title>Nordisk Husforum</title>
<link href="https://fonts.googleapis.com/css2?family=Arimo&display=swap" rel="stylesheet">
<style>
  :root {
    --red: #a3000b;
    --red-dark: #7d0008;
    --red-deep: #6a0006;
    --line: #e9b5b5;
    --white: #ffffff;
    --tab: #8c0610;
    --photo-warm: #b88a6a;
    --photo-cafe: #b99a86;
    --photo-night: #4a5a82;
    --photo-corner: #a84a3e;
  }
  html, body { margin: 0; padding: 0; overflow: hidden; }
  body { width: 1200px; height: 900px; font-family: "Arimo", Arial, sans-serif; color: var(--white); }
  .canvas {
    position: relative; width: 1200px; height: 900px; overflow: hidden;
    background: linear-gradient(180deg, var(--red-dark) 0, var(--red) 126px, var(--red) 815px, var(--red-deep) 900px);
  }
  .abs { position: absolute; }
  .rule-h { position: absolute; left: 0; width: 1200px; height: 2px; background: var(--line); }
  .rule-v { position: absolute; top: 165px; width: 3px; height: 650px; background: var(--white); }
  .brand { left: 46px; top: 80px; font-size: 28px; letter-spacing: 0.5px; }
  .nav a { position: absolute; top: 131px; height: 28px; line-height: 28px; font-size: 28px; color: var(--white);
    text-decoration: none; background: var(--tab); text-align: center; }
  .photo { position: absolute; }
  .p-warm { background: linear-gradient(180deg, #d9b9a4, var(--photo-warm) 50%, #6e5a4c); }
  .p-cafe { background: linear-gradient(180deg, #e6cfc0, var(--photo-cafe) 55%, #5a4a44); }
  .p-night { background: linear-gradient(180deg, #6e88b8, var(--photo-night) 55%, #2a2a34); }
  .p-corner { background: linear-gradient(180deg, #e0dcd6, var(--photo-corner) 55%, #7a6a5e); }
  .listing-title { position: absolute; font-size: 28px; }
  .listing-info { position: absolute; font-size: 14px; line-height: 19px; }
  .listing-info .name { padding-left: 2px; }
  .side-title { left: 907px; width: 296px; top: 194px; text-align: center; font-size: 28px; }
  .sold { position: absolute; left: 907px; width: 300px; text-align: center; font-size: 28px; }
  .more { position: absolute; top: 770px; font-size: 28px; }
  .footer-copy { left: 38px; top: 829px; font-size: 14px; }
  .footer-links { left: 347px; top: 827px; font-size: 14px; word-spacing: 1px; }
  .footer-links span { margin-right: 14px; }
  .sale-badge { left: 620px; top: 0; }
</style>
</head>
<body>
<div class="canvas">
  <svg class="abs sale-badge" width="150" height="110" viewBox="0 0 150 110" aria-hidden="false">
    <polygon points="62,-10 80,18 118,8 108,42 140,60 104,72 104,104 76,86 50,106 44,72 10,62 40,44 22,12 56,20" fill="#c4000e"/>
    <g fill="#ffffff" font-family="Arimo, Arial, sans-serif" font-size="22" transform="rotate(-30 80 50)">
      <text x="40" y="38">SALE</text>
      <text x="48" y="60">SALE</text>
      <text x="56" y="82">SALE</text>
    </g>
  </svg>

  <div class="photo p-cafe" style="left:765px;top:18px;width:121px;height:85px" role="img" aria-label="Photo of a café and bar front"></div>
  <div class="photo p-warm" style="left:908px;top:18px;width:114px;height:85px" role="img" aria-label="Photo of a restaurant front"></div>
  <div class="photo p-night" style="left:1039px;top:18px;width:108px;height:85px" role="img" aria-label="Photo of a round corner building at night"></div>

  <div class="abs brand">Nordisk Husforum</div>

  <div class="rule-h" style="top:125px"></div>
  <nav class="nav">
    <a href="#" style="left:44px;width:103px">Home</a>
    <a href="#" style="left:183px;width:115px">On Sell</a>
    <a href="#" style="left:325px;width:157px">Achivment</a>
    <a href="#" style="left:514px;width:168px">Contact Us</a>
  </nav>
  <div class="rule-h" style="top:164px"></div>

  <div class="photo p-warm" style="left:91px;top:183px;width:240px;height:181px" role="img" aria-label="Photo of a restaurant on the main road"></div>
  <div class="listing-title" style="left:369px;top:184px">On Sell</div>
  <div class="listing-info" style="left:473px;top:216px"><div class="name">Restaurant on Main road</div><div>Area- 3000 Sq Ft</div><div>Price- 56000$</div></div>

  <div class="photo p-cafe" style="left:91px;top:388px;width:240px;height:166px" role="img" aria-label="Photo of a café on Street No. 4"></div>
  <div class="listing-title" style="left:367px;top:388px">On Sell</div>
  <div class="listing-info" style="left:473px;top:421px"><div class="name">Cafe on Street No.-4</div><div>Area- 2500 Sq Ft</div><div>Price- 66000$</div></div>

  <div class="photo p-cafe" style="left:91px;top:594px;width:240px;height:167px" role="img" aria-label="Photo of a café and bar on Street No. 8"></div>
  <div class="listing-title" style="left:369px;top:595px">On Sell</div>
  <div class="listing-info" style="left:473px;top:628px"><div class="name">Cafe &amp; Bar on Street No.-8</div><div>Area- 4500 Sq Ft</div><div>Price- 86000$</div></div>

  <div class="more" style="left:671px">More….</div>

  <div class="rule-v" style="left:858px"></div>
  <div class="rule-v" style="left:906px"></div>

  <div class="abs side-title">Achivment</div>
  <div class="photo p-night" style="left:959px;top:254px;width:194px;height:153px" role="img" aria-label="Photo of a sold round corner building at night"></div>
  <div class="sold" style="top:413px">Successfuly Sold</div>
  <div class="photo p-corner" style="left:957px;top:494px;width:196px;height:206px" role="img" aria-label="Photo of a sold corner café"></div>
  <div class="sold" style="top:702px">Successfuly Sold</div>
  <div class="more" style="left:1087px">More….</div>

  <div class="rule-h" style="top:814px;height:3px;background:var(--white)"></div>

  <div class="abs footer-copy">Copyright- Nordisk Husforum</div>
  <div class="abs footer-links"><span>Pubs on Sell</span><span>Bar on Sell</span><span>Hotel on Sell</span><span>Restaurant on Sell</span><span>Plot on Sell</span><span>A/C Bar on Sell</span></div>
</div>
</body>
</html>
```